Creative & Professional Business Card for hair salon

We are looking to update our business cards. Our salon is creative, modern, progressive and professional and looking for a design that will reflect this.

```html
<!DOCTYPE html>
<html lang="en">
<head>
<meta charset="utf-8">
<title>Silver Loom Studio – Business Card</title>
<link rel="stylesheet" href="https://fonts.googleapis.com/css2?family=Lato:wght@300;400;700&display=swap">
<style>
  :root {
    --backdrop: #4a7594;
    --card: #ffffff;
    --brand-blue: #2f5f84;
    --brand-teal: #5a94ad;
    --ink: #2b2b2b;
    --muted: #5b5b5b;
    --rule: #d8dde2;
    --rule-dark: #8a9096;
    --ghost: #eef3f6;
  }
  * { margin: 0; padding: 0; box-sizing: border-box; }
  html, body { width: 1200px; height: 900px; overflow: hidden; }
  body {
    background: var(--backdrop);
    font-family: "Lato", sans-serif;
    position: relative;
  }
  .card {
    position: absolute;
    top: 275px;
    width: 477px;
    height: 295px;
    background: var(--card);
    box-shadow: 2px 4px 5px rgba(0, 0, 0, 0.45);
    overflow: hidden;
  }
  .card--front { left: 120px; border-radius: 8px 46px 4px 46px; }
  .card--back  { left: 607px; border-radius: 46px 4px 46px 4px; }

  /* Front */
  .brand {
    position: absolute;
    right: 25px;
    top: 108px;
    text-align: right;
    color: var(--brand-teal);
    font-weight: 300;
  }
  .brand__name { font-size: 23px; line-height: 1; }
  .brand__by { font-size: 12px; margin-top: 5px; }

  .person { position: absolute; left: 30px; top: 163px; right: 25px; }
  .person__name {
    font-size: 18px; font-weight: 700; color: var(--brand-blue);
    letter-spacing: 0.2px; line-height: 1;
  }
  .person__role {
    display: flex; align-items: center; gap: 4px;
    font-size: 13px; color: var(--ink); margin-top: 5px;
  }
  .person__role::after {
    content: ""; flex: 1; height: 1px; background: var(--rule); margin-top: 4px;
  }

  .contact {
    position: absolute; top: 217px; list-style: none;
    font-size: 13.5px; color: var(--ink); line-height: 18px;
  }
  .contact--left { left: 30px; }
  .contact--right { right: 25px; text-align: right; }
  .contact li { display: flex; align-items: center; gap: 5px; }
  .contact--right li { justify-content: flex-end; }
  .contact svg { width: 11px; height: 11px; fill: var(--brand-blue); flex: none; }
  .contact .dot { width: 15px; height: 15px; border-radius: 50%; background: var(--brand-blue); flex: none; }

  /* Back */
  .ghost-mark {
    position: absolute; left: 0; top: 40px; width: 477px;
    text-align: center; font-size: 72px; font-weight: 300;
    color: var(--ghost); line-height: 1; white-space: nowrap;
  }
  .appointment__title {
    position: absolute; left: 0; right: 0; top: 77px;
    text-align: center; font-size: 20px; color: var(--brand-blue);
    letter-spacing: 0.3px;
  }
  .appointment__field {
    position: absolute; left: 80px; width: 315px;
    display: flex; align-items: flex-end;
    font-size: 18px; color: var(--brand-blue);
  }
  .appointment__field--date { top: 139px; }
  .appointment__field--time { top: 180px; }
  .appointment__field span { width: 65px; }
  .appointment__field i {
    flex: 1; height: 1px; background: var(--rule-dark); margin-bottom: 5px;
  }
  .appointment__notice {
    position: absolute; left: 0; right: 0; top: 254px;
    text-align: center; font-size: 13.5px; color: var(--muted);
  }
</style>
</head>
<body>
  <section class="card card--front">
    <div class="brand">
      <div class="brand__name">Silver Loom Studio</div>
      <div class="brand__by">by Mara Dellen</div>
    </div>
    <div class="person">
      <div class="person__name">DANIEL OKORO</div>
      <div class="person__role">Managing Director</div>
    </div>
    <ul class="contact contact--left">
      <li><svg viewBox="0 0 12 12"><path d="M1 4c0-2 2-3 5-3s5 1 5 3l-2 1-1-1.5H4L3 5 1 4zm2 2h6l1 5H2l1-5zm3 1a1.5 1.5 0 1 0 0 3 1.5 1.5 0 0 0 0-3z"/></svg>021-555 0184 32</li>
      <li><svg viewBox="0 0 12 12"><path d="M1 2.5h10v7H1zM1.5 3l4.5 3.5L10.5 3v1L6 7.5 1.5 4z" fill-rule="evenodd"/></svg>hello@silverloom.com</li>
      <li><svg viewBox="0 0 12 12"><circle cx="6" cy="6" r="5"/></svg>www.silverloom.com</li>
    </ul>
    <ul class="contact contact--right">
      <li>social.silverloom.com <span class="dot"></span></li>
      <li>18, Willow Arcade</li>
      <li>30917 Eastmere</li>
    </ul>
  </section>

  <section class="card card--back">
    <div class="ghost-mark" aria-hidden="true">Silver Loom</div>
    <h2 class="appointment__title" style="font-weight:400">YOUR NEXT APPOINTMENT</h2>
    <div class="appointment__field appointment__field--date"><span>DATE:</span><i></i></div>
    <div class="appointment__field appointment__field--time"><span>TIME:</span><i></i></div>
    <p class="appointment__notice">If unable to keep appointment, kindly give 24hrs notice.</p>
  </section>
</body>
</html>
```